the halvorsen group premier division

design a DL A4 tri fold brochure to reflect our creative landscape business
my web site www.thehalvorsengroup.com.au
has all the information needed
i will also be updating the website to be more updated and creative design

```html
<!DOCTYPE html>
<html lang="en">
<head>
<meta charset="utf-8">
<title>The Halvorsen Group Premier Division – Tri-fold Brochure</title>
<link rel="stylesheet" href="https://fonts.googleapis.com/css2?family=Montserrat:wght@400;500;600;700&display=swap">
<style>
  :root {
    --page-bg: #a7a7a7;
    --paper: #e4e4e4;
    --paper-dark: #cfcfcf;
    --orange: #d0631c;
    --amber: #e9a233;
    --ink: #3b3b3b;
    --white: #ffffff;
    --leaf: #c9cfcb;
  }
  * { box-sizing: border-box; margin: 0; padding: 0; }
  html, body { width: 1200px; height: 907px; overflow: hidden; }
  body {
    background: var(--page-bg);
    font-family: "Montserrat", Arial, sans-serif;
    position: relative;
  }
  .brochure {
    position: absolute;
    left: 60px; top: 71px;
    width: 1080px; height: 764px;
    display: flex;
  }
  .panel { position: relative; width: 360px; height: 764px; overflow: hidden; }

  /* Left panel – services */
  .panel--services { background: linear-gradient(160deg, var(--paper) 0%, var(--paper-dark) 100%); }
  .service-list {
    position: absolute;
    list-style: none;
    color: var(--orange);
    font-size: 19px; line-height: 1.2; font-weight: 400;
    white-space: nowrap;
  }
  .service-list--top { top: 56px; left: 48px; }
  .service-list--bottom { top: 552px; left: 26px; }
  .photo { position: absolute; }
  .photo--garden-front {
    left: 40px; top: 168px; width: 196px; height: 350px;
    background: linear-gradient(170deg, #8a949b 0%, #6f7d5a 35%, #566b3b 65%, #7a6b58 100%);
  }
  .photo--pot-plant {
    left: 236px; top: 656px; width: 88px; height: 100px;
    background: radial-gradient(ellipse at 50% 40%, #2f7a2c 0%, #3f8a35 45%, rgba(220,220,220,0) 72%);
  }
  .leaf-decor {
    position: absolute;
    background: radial-gradient(ellipse, var(--leaf) 0%, rgba(201,207,203,0) 70%);
  }
  .leaf-decor--services { left: 110px; top: -20px; width: 200px; height: 130px; }

  /* Middle panel – contact */
  .panel--contact {
    background: linear-gradient(180deg, #c46a28 0%, #d88a45 35%, #c9772f 65%, #b9631f 100%);
  }
  .photo--garden-path {
    inset: 0;
    background: linear-gradient(160deg, rgba(233,170,110,0.45) 0%, rgba(150,110,60,0.35) 50%, rgba(120,90,40,0.4) 100%);
  }
  .logo-box {
    position: absolute;
    display: flex; align-items: center; justify-content: center; gap: 12px;
    background: var(--white);
  }
  .logo-box--contact { left: 28px; top: 42px; width: 304px; height: 170px; }
  .brand-mark { width: 22px; height: 22px; border-radius: 50%; background: var(--amber); flex: none; }
  .brand-name {
    color: var(--ink); font-weight: 700; text-align: center;
    font-size: 22px; line-height: 1.15;
  }
  .contact {
    position: absolute; left: 0; right: 0; top: 238px;
    text-align: center; color: var(--white);
    font-size: 14.5px; font-weight: 600; line-height: 1.45;
  }
  .contact p { margin-bottom: 14px; }

  /* Right panel – cover */
  .panel--cover { background: linear-gradient(180deg, var(--paper) 0%, #dedede 100%); }
  .photo--courtyard {
    left: 0; top: 0; width: 360px; height: 400px;
    background: linear-gradient(160deg, #b8bcbd 0%, #8e9a8a 35%, #5f7a45 60%, #6e6258 100%);
  }
  .logo-frame {
    position: absolute; left: 104px; top: 330px; width: 222px; height: 152px;
    border: 3px solid var(--amber);
  }
  .logo-box--cover { left: 118px; top: 344px; width: 194px; height: 124px; gap: 8px; padding: 0 8px; }
  .logo-box--cover .brand-name { font-size: 13px; }
  .logo-box--cover .brand-mark { width: 12px; height: 12px; }
  .cover-title {
    position: absolute; left: 42px; top: 538px;
    color: var(--ink); font-size: 30px; font-weight: 700; line-height: 1.22;
    white-space: nowrap;
  }
  .cover-rule {
    position: absolute; left: 42px; top: 668px; width: 262px; height: 3px;
    background: var(--amber);
  }
  .leaf-decor--cover-top { left: -30px; top: 400px; width: 150px; height: 160px; }
  .leaf-decor--cover-bottom { left: 150px; top: 660px; width: 220px; height: 130px; }
</style>
</head>
<body>
  <main class="brochure">
    <section class="panel panel--services">
      <div class="leaf-decor leaf-decor--services" role="img" aria-label="Faint monstera leaf decoration"></div>
      <ul class="service-list service-list--top">
        <li>Bespoke Structural Features</li>
        <li>Water Features</li>
        <li>Paving &amp; Pathways</li>
        <li>Concreting and Aggregate</li>
      </ul>
      <div class="photo photo--garden-front" role="img" aria-label="Photo of a planted front garden with stone path before a weatherboard house"></div>
      <ul class="service-list service-list--bottom">
        <li>Plant &amp; Tree supply &amp; installation</li>
        <li>Earth Preparation</li>
        <li>Lawns</li>
        <li>Irrigation Systems</li>
      </ul>
      <div class="photo photo--pot-plant" role="img" aria-label="Potted leafy plant in a white pot"></div>
    </section>

    <section class="panel panel--contact">
      <div class="photo photo--garden-path" role="img" aria-label="Orange-toned photo of a paved garden path lined with shrubs"></div>
      <div class="logo-box logo-box--contact">
        <span class="brand-mark"></span>
        <span class="brand-name">The Halvorsen Group<br>Premier Division</span>
      </div>
      <div class="contact">
        <p>Ben Marlowe The Halvorsen Group<br>Premier Division</p>
        <p>Postal: PO BOX 208 Westhaven VIC 3099</p>
        <p>Tel: 0400 318 642</p>
        <p>Email:info@thehalvorsengroup.com.au</p>
        <p>Visit us at Show Stand B12<br>Fri 8 — Mon 11 Sep 2017.<br>Riverside Expo Hall, Eastbank.</p>
      </div>
    </section>

    <section class="panel panel--cover">
      <div class="photo photo--courtyard" role="img" aria-label="Photo of a modern courtyard with white outdoor furniture, paving and greenery"></div>
      <div class="leaf-decor leaf-decor--cover-top" role="img" aria-label="Faint monstera leaf decoration"></div>
      <div class="logo-frame"></div>
      <div class="logo-box logo-box--cover">
        <span class="brand-mark"></span>
        <span class="brand-name">The Halvorsen Group<br>Premier Division</span>
      </div>
      <h1 class="cover-title">Creative<br>Landscape Design<br>&amp; Construction</h1>
      <div class="cover-rule"></div>
      <div class="leaf-decor leaf-decor--cover-bottom" role="img" aria-label="Faint monstera leaf decoration"></div>
    </section>
  </main>
</body>
</html>
```